Pharmacy Benefit Manager needs grahics for marketing material

We have a logo. We need integrated graphics we can use for proposal cover sheets and a power point template. I am including our logo and our business cards. We do not want to use pills, prescription bottles or other pharmacy related objects.

Marketing

```html
<!DOCTYPE html>
<html lang="en">
<head>
<meta charset="utf-8">
<title>Verano – Proposal Cover</title>
<link rel="stylesheet" href="https://fonts.googleapis.com/css2?family=Open+Sans:wght@400;600;700;800&display=swap">
<style>
  :root {
    --paper: #e6e6e6;
    --ink: #261a08;
    --leaf: #5e9a34;
    --text-dark: #231f20;
  }
  * { margin: 0; padding: 0; box-sizing: border-box; }
  html, body {
    width: 849px;
    height: 1200px;
    overflow: hidden;
    background: var(--paper);
  }
  .cover {
    position: relative;
    width: 849px;
    height: 1200px;
    background: var(--paper);
    font-family: "Open Sans", Arial, sans-serif;
    overflow: hidden;
  }
  .cover__artwork {
    position: absolute;
    left: 0;
    top: 0;
    width: 849px;
    height: 1010px;
    background: linear-gradient(125deg, var(--ink) 0%, var(--ink) 45%, var(--leaf) 75%, var(--leaf) 100%);
    clip-path: polygon(0 0, 100% 0, 100% 42%, 93% 63%, 80% 100%, 51% 90%, 0 63%);
  }
  .brand {
    position: absolute;
    left: 97px;
    top: 1030px;
    width: 362px;
  }
  .brand__name {
    display: block;
    font-weight: 800;
    font-size: 82px;
    line-height: 1;
    letter-spacing: -1px;
    color: var(--text-dark);
    padding-left: 38px;
  }
  .brand__mark {
    position: absolute;
    left: 376px;
    top: 10px;
    font-size: 10px;
    font-weight: 600;
    color: var(--text-dark);
  }
  .brand__rule {
    display: block;
    height: 2px;
    background: var(--text-dark);
    margin-top: 6px;
  }
  .brand__tagline {
    display: block;
    font-size: 14.5px;
    font-weight: 600;
    color: var(--text-dark);
    margin-top: 3px;
    letter-spacing: 0.1px;
  }
  .cover__web {
    position: absolute;
    left: 683px;
    top: 1144px;
    font-size: 11px;
    color: var(--leaf);
  }
</style>
</head>
<body>
  <main class="cover">
    <div class="cover__artwork" role="img" aria-label="Large curved grid pattern of dark brown and green tiles"></div>

    <div class="brand">
      <span class="brand__name">Verano</span>
      <span class="brand__mark">SM</span>
      <span class="brand__rule"></span>
      <span class="brand__tagline">prescription benefit management</span>
    </div>

    <p class="cover__web">www.veranopbm.com</p>
  </main>
</body>
</html>
```